BUSINESS CONSULTING

Would like a page design that would reflect "flow" effect that denotes moving around obstacles and logo webpage for Brenmark Consulting. We provide business consulting in the areas of training/facilitation, Leadership Coaching and Development, Process Improvement and Employee On-boarding and Authorization.

Need skeletal designed to be populated at a later date.

Industry/Entity Type

Business

```html
<!DOCTYPE html>
<html lang="en">
<head>
<meta charset="utf-8">
<title>Brenmark Logistics</title>
<link href="https://fonts.googleapis.com/css2?family=Carlito:wght@400;700&display=swap" rel="stylesheet">
<style>
  :root {
    --brand-blue: #0a7bbd;
    --brand-red: #d10a0a;
    --ink: #2b2b2b;
    --muted: #444;
    --white: #ffffff;
    --caption-blue: rgba(23, 125, 172, 0.9);
    --caption-grey: rgba(60, 60, 56, 0.88);
    --rule: #b9b9b9;
    --hero-top: #5a78c4;
    --hero-mid: #b8b4cf;
    --hero-low: #8a8c90;
  }
  * { box-sizing: border-box; margin: 0; padding: 0; }
  html, body { width: 1200px; height: 948px; overflow: hidden; background: var(--white); }
  body { position: relative; font-family: "Carlito", "Calibri", sans-serif; color: var(--ink); }

  .site-header { position: absolute; top: 0; left: 0; width: 1200px; height: 94px; border-top: 3px solid var(--brand-blue); }
  .brand-name { position: absolute; left: 151px; top: 18px; font-size: 37px; font-weight: 700; color: var(--brand-blue); letter-spacing: 0.3px; line-height: 1; }
  .phone-tab { position: absolute; left: 900px; top: 0; width: 148px; height: 33px; background: var(--brand-blue); border-radius: 0 0 18px 18px; color: var(--white); font-family: Arial, sans-serif; font-weight: 700; font-size: 15px; display: flex; align-items: center; justify-content: center; gap: 6px; box-shadow: 0 3px 4px rgba(0,0,0,0.15); }
  .main-nav { position: absolute; right: 150px; top: 60px; display: flex; gap: 30px; }
  .main-nav a { font-size: 14px; color: var(--ink); text-decoration: none; text-transform: uppercase; letter-spacing: 0.4px; }

  .hero { position: absolute; top: 94px; left: 0; width: 1200px; height: 422px; overflow: hidden;
    background: linear-gradient(180deg, var(--hero-top) 0%, var(--hero-mid) 55%, var(--hero-low) 100%); }
  .hero-arrow { position: absolute; top: 178px; }
  .hero-arrow.prev { left: 67px; }
  .hero-arrow.next { left: 1099px; }
  .hero-caption { position: absolute; font-family: Arial, sans-serif; font-size: 26px; color: var(--white); line-height: 37px; padding: 0 6px; }
  .hero-caption.primary { left: 152px; top: 268px; background: var(--caption-blue); }
  .hero-caption.secondary { left: 240px; top: 306px; background: var(--caption-grey); }

  .section-title { font-size: 26px; font-weight: 400; color: var(--brand-blue); letter-spacing: 0.5px; line-height: 1; }
  .about { position: absolute; left: 151px; top: 556px; width: 580px; }
  .about p { font-size: 12.4px; line-height: 16px; color: var(--muted); text-align: justify; margin-top: 14px; }
  .about p + p { margin-top: 15px; }
  .read-more { display: inline-block; margin-top: 22px; background: var(--brand-red); color: var(--white); font-family: Arial, sans-serif; font-size: 14px; line-height: 28px; padding: 0 12px; text-decoration: none; }

  .column-divider { position: absolute; left: 771px; top: 544px; width: 14px; height: 262px; background: linear-gradient(90deg, rgba(0,0,0,0.08), rgba(0,0,0,0)); -webkit-mask: linear-gradient(180deg, transparent, #000 20%, #000 80%, transparent); mask: linear-gradient(180deg, transparent, #000 20%, #000 80%, transparent); }

  .services { position: absolute; left: 809px; top: 556px; width: 240px; }
  .service-list { list-style: none; margin-top: 16px; }
  .service-list li { position: relative; padding: 0 0 7px 25px; font-size: 16px; line-height: 17px; color: var(--ink); letter-spacing: 0.3px; border-bottom: 1px dotted var(--rule); margin-bottom: 8px; }
  .service-list li:last-child { border-bottom: none; }
  .service-list svg { position: absolute; left: 0; top: 2px; }

  .site-footer { position: absolute; left: 0; top: 872px; width: 1200px; height: 76px; background: var(--brand-blue); color: var(--white); }
  .footer-nav { position: absolute; left: 151px; top: 17px; font-size: 13.5px; letter-spacing: 0.2px; }
  .footer-nav a { color: var(--white); text-decoration: none; }
  .footer-nav .sep { margin: 0 7px; }
  .copyright { position: absolute; left: 151px; top: 38px; font-size: 13px; letter-spacing: 0.2px; }
  .footer-brand { position: absolute; right: 150px; top: 18px; font-size: 30px; font-weight: 700; line-height: 1; color: var(--white); }
</style>
</head>
<body>
  <header class="site-header">
    <div class="brand-name">BRENMARK</div>
    <div class="phone-tab">
      <svg width="10" height="16" viewBox="0 0 10 16" aria-hidden="true"><path d="M3 1 L6 1 L6 4 L4.5 5 Q4 8 4.5 11 L6 12 L6 15 L3 15 Q0 8 3 1 Z" fill="#fff"/></svg>
      555-014-2290
    </div>
    <nav class="main-nav">
      <a href="#">Home</a>
      <a href="#">About Us</a>
      <a href="#">Our Services</a>
      <a href="#">Partnership Overview</a>
      <a href="#">Contact Us</a>
    </nav>
  </header>

  <section class="hero">
    <div role="img" aria-label="Photo of a transport truck on a highway at sunrise" style="position:absolute;inset:0;"></div>
    <svg class="hero-arrow prev" width="36" height="68" viewBox="0 0 36 68" aria-hidden="true"><polyline points="35,1 2,34 35,67" fill="none" stroke="#fff" stroke-width="2"/></svg>
    <svg class="hero-arrow next" width="36" height="68" viewBox="0 0 36 68" aria-hidden="true"><polyline points="1,1 34,34 1,67" fill="none" stroke="#fff" stroke-width="2"/></svg>
    <div class="hero-caption primary">Lorem ipsum dolor sit amet</div>
    <div class="hero-caption secondary">Consectetur adipiscing elit</div>
  </section>

  <section class="about">
    <h2 class="section-title">WHO WE ARE</h2>
    <p>Lorem ipsum dolor sit amet, consectetur adipiscing elit. Nunc iaculis purus nec massa commodo pellentesque. Sed lobortis nisi ligula, in ullamcorper eros vulputate eget. Sed sit amet erat gravida, auctor nisi vitae, placerat odio. Integer aliquam adipiscing semper. Donec vel lacus id nunc ullamcorper convallis. Morbi velit risus, vehicula eget lacinia vel, rutrum nec velit. Aliquam posuere velit nibh, eget fermentum enim viverra interdum. Donec auctor tempor vestibulum.</p>
    <p>Maecenas non nunc scelerisque ipsum fermentum dignissim a a libero. Cum sociis natoque penatibus et magnis dis parturient montes, nascetur ridiculus mus. Nunc tempus magna justo, vel lacinia eros volutpat ac. Fusce varius rutrum risus, mollis ornare nisi ornare in. Aenean tempor commodo purus. Suspendisse vel suscipit elit, vel eleifend ligula. Donec ac tincidunt urna.</p>
    <a class="read-more" href="#">Read More</a>
  </section>

  <div class="column-divider"></div>

  <section class="services">
    <h2 class="section-title">WHAT WE DO</h2>
    <ul class="service-list">
      <li><svg width="17" height="12" viewBox="0 0 17 12" aria-hidden="true"><path d="M0 4.5 H10 V0 L17 6 L10 12 V7.5 H0 Z" fill="#d10a0a"/></svg>Transportation Management Solutions</li>
      <li><svg width="17" height="12" viewBox="0 0 17 12" aria-hidden="true"><path d="M0 4.5 H10 V0 L17 6 L10 12 V7.5 H0 Z" fill="#d10a0a"/></svg>Distribution &amp; Warehouse Management</li>
      <li><svg width="17" height="12" viewBox="0 0 17 12" aria-hidden="true"><path d="M0 4.5 H10 V0 L17 6 L10 12 V7.5 H0 Z" fill="#d10a0a"/></svg>Technology Solutions</li>
      <li><svg width="17" height="12" viewBox="0 0 17 12" aria-hidden="true"><path d="M0 4.5 H10 V0 L17 6 L10 12 V7.5 H0 Z" fill="#d10a0a"/></svg>Process Improvement &amp; Consulting Services</li>
    </ul>
  </section>

  <footer class="site-footer">
    <nav class="footer-nav">
      <a href="#">Home</a><span class="sep">|</span><a href="#">About us</a><span class="sep">|</span><a href="#">Our Services</a><span class="sep">|</span><a href="#">Partnership Overview</a><span class="sep">|</span><a href="#">Contact us</a>
    </nav>
    <div class="copyright">Copyright © 2014 BRENMARK Logistics, LLC</div>
    <div class="footer-brand">BRENMARK</div>
  </footer>
</body>
</html>
```